Morrow & Pellant Stationery

Greetings again. Now we've got an awesome logo, it's time to get the stationery to go with it. We require the following items of stationery:

- Business Card - Print Ready, all we need to do is change names and numbers and submit to printer.  Double sided with logo on one side and details on the other side. (85mm x 55mm)

- With Compliments Slip

- Letterhead - These will be preprinted pages that will then be used as pages.
(A4)

- Envelope - Business Size(Standard DL)

Target Market(s)

Essentially, this firm services clients facing criminal charges and/or seeking legal aid. The firm is also looking at taking on more white-collar crime cases.

Requirements
Must have
• - Same Design Cues & Colours as the Branding details attached

• - Address (as follows)

• Suite 8

• 212-216 Carrow St

• HARLOWE VIC 3990

• Phone: (03) 9555 0142

• Fax: (03) 9555 0187

• Web: www.morrowandpellant.example

• - Colour: Pantone 194 (Red)

```html
<!DOCTYPE html>
<html lang="en">
<head>
<meta charset="utf-8">
<title>Morrow &amp; Pellant Stationery</title>
<link rel="stylesheet" href="https://fonts.googleapis.com/css2?family=Cinzel:wght@400;600&family=Open+Sans:wght@400&display=swap">
<style>
  :root {
    --backdrop: #6b6b6b;
    --paper: #ffffff;
    --frame-grey: #c4c4c4;
    --brand-red: #a51c30;
    --brand-red-dark: #8a1627;
    --ink: #2a2a2a;
    --muted: #8c8c8c;
    --faint: #b9b9b9;
    --decor: #d4d4d4;
    --card-black: #050505;
  }
  * { box-sizing: border-box; margin: 0; padding: 0; }
  html, body { width: 1200px; height: 883px; overflow: hidden; }
  body { background: var(--backdrop); position: relative; font-family: "Cinzel", serif; }

  /* Shared brand lockup */
  .brand { display: flex; align-items: center; gap: 8px; }
  .brand__dot { border-radius: 50%; background: var(--brand-red); flex: none; }
  .brand__name { font-weight: 600; color: var(--ink); line-height: 1.05; white-space: nowrap; }
  .brand__tag { font-weight: 600; color: var(--ink); line-height: 1.05; white-space: nowrap; }

  /* Letterhead */
  .letterhead {
    position: absolute; left: 241px; top: 0; width: 569px; height: 865px;
    background: var(--paper);
    border: 5px solid var(--frame-grey);
    box-shadow: 4px 4px 8px rgba(0,0,0,.35);
  }
  .letterhead__edge {
    position: absolute; left: 809px; top: 19px; width: 11px; height: 846px;
    background: var(--brand-red-dark);
  }
  .letterhead__brand {
    position: absolute; left: 128px; top: 745px; gap: 14px;
  }
  .letterhead__brand .brand__dot { width: 62px; height: 62px; background: var(--decor); }
  .letterhead__brand .brand__rule { width: 1px; height: 56px; background: var(--decor); }
  .letterhead__brand .brand__name { color: var(--faint); font-size: 22px; font-weight: 400; }
  .letterhead__brand .brand__tag { color: var(--faint); font-size: 15px; font-weight: 400; }
  .letterhead__footer {
    position: absolute; left: 0; right: 0; bottom: 4px;
    text-align: center; font-family: "Open Sans", sans-serif;
    font-size: 6px; color: var(--muted); letter-spacing: .3px; white-space: nowrap;
  }

  /* Envelope */
  .envelope {
    position: absolute; left: 509px; top: 422px; width: 676px; height: 324px;
    background: var(--paper);
    border: 20px solid var(--frame-grey);
    box-shadow: 14px 14px 10px rgba(0,0,0,.55);
  }
  .envelope .brand { position: absolute; left: 6px; top: 0; }
  .envelope .brand__dot { width: 44px; height: 44px; }
  .envelope .brand__name { font-size: 16px; }
  .envelope .brand__tag { font-size: 10px; }

  /* Business card */
  .card {
    position: absolute; left: 143px; top: 441px; width: 159px; height: 268px;
    background: var(--paper); overflow: hidden;
  }
  .card__band { position: absolute; left: 0; top: 0; width: 100%; height: 32px; background: var(--card-black); }
  .card__details {
    position: absolute; left: 0; right: 0; top: 38px; text-align: center;
    color: var(--muted); font-size: 7px; line-height: 1.3; letter-spacing: 1px; text-transform: uppercase;
  }
  .card__details .card__person { font-size: 9px; letter-spacing: 1.6px; }
  .card__details .card__email {
    font-family: "Open Sans", sans-serif; text-transform: none; font-size: 4px; letter-spacing: .2px; margin-top: 3px;
  }
  .card__decor {
    position: absolute; left: 10px; top: 100px; width: 130px; height: 130px;
    border-radius: 50%; background: var(--decor); opacity: .7;
  }
  .card .brand { position: absolute; left: 6px; top: 212px; gap: 5px; }
  .card .brand__dot { width: 34px; height: 34px; }
  .card .brand__name { font-size: 10px; }
  .card .brand__tag { font-size: 6.5px; }
  .card__web {
    position: absolute; left: 0; bottom: 0; width: 100%; height: 15px;
    background: var(--brand-red); color: var(--paper);
    font-family: "Open Sans", sans-serif; font-size: 5px; letter-spacing: .6px;
    display: flex; align-items: center; justify-content: center; text-transform: uppercase;
  }
</style>
</head>
<body>

  <section class="letterhead" aria-label="Letterhead">
    <div class="letterhead__brand brand">
      <span class="brand__dot"></span>
      <span class="brand__rule"></span>
      <div>
        <div class="brand__name">Morrow &amp; Pellant</div>
        <div class="brand__tag">Barristers &amp; Solicitors</div>
      </div>
    </div>
    <p class="letterhead__footer">212-216 Carrow St, Suite 8, Harlowe VIC 3990 &nbsp;|&nbsp; P (03) 9555 0142 &nbsp;|&nbsp; F (03) 9555 0187 &nbsp;|&nbsp; info@morrowandpellant.example &nbsp;|&nbsp; www.morrowandpellant.example</p>
  </section>
  <div class="letterhead__edge"></div>

  <section class="envelope" aria-label="DL envelope">
    <div class="brand">
      <span class="brand__dot"></span>
      <div>
        <div class="brand__name">Morrow &amp; Pellant</div>
        <div class="brand__tag">Barristers &amp; Solicitors</div>
      </div>
    </div>
  </section>

  <section class="card" aria-label="Business card">
    <div class="card__band"></div>
    <div class="card__details">
      <div class="card__person">Daniel Harker</div>
      <div>212-216 Carrow St, Suite 8</div>
      <div>Harlowe VIC 3990</div>
      <div>P (03) 9555 0142</div>
      <div>F (03) 9555 0187</div>
      <div class="card__email">daniel@morrowandpellant.example</div>
    </div>
    <div class="card__decor"></div>
    <div class="brand">
      <span class="brand__dot"></span>
      <div>
        <div class="brand__name">Morrow &amp; Pellant</div>
        <div class="brand__tag">Barristers &amp; Solicitors</div>
      </div>
    </div>
    <div class="card__web">www.morrowandpellant.example</div>
  </section>

</body>
</html>
```